lunch and dinne(al a carte) menus

we are a medium sized licenced club that has taken back the dining in the club
in the western suburbs of sydney working class with a rugby league base
our logo is a wolf kelford hawks

Reason: We have changed the name to Bluegate grill it could be done as Bluegate or Bluegate or Bluegate We need a lunch menu and a seperate dinner menu eg Bluegate grill l u n c h or Bluegate grill d i n n e r

Reason: Weve changed the name

Target Market(s)

young families, working class rugby leagues sporty types

Industry/Entity Type

Club

Requirements
Must have
• user friendly

```html
<!DOCTYPE html>
<html lang="en">
<head>
<meta charset="utf-8">
<title>Bluegate grill – Lunch &amp; Dinner Menus</title>
<link href="https://fonts.googleapis.com/css2?family=Archivo+Narrow:ital,wght@0,400;0,600;1,400&family=Open+Sans:ital,wght@0,700;0,800;1,400&family=Signika:wght@400;600&display=swap" rel="stylesheet">
<style>
  :root {
    --green: #1f8a3a;
    --green-deep: #17742f;
    --pale: #fbf9d6;
    --gold: #f2b21a;
    --ink: #141414;
    --white: #ffffff;
    --paper: #ffffff;
  }
  * { box-sizing: border-box; margin: 0; padding: 0; }
  html, body { width: 1200px; height: 900px; overflow: hidden; background: var(--paper); }
  .canvas { position: relative; width: 1200px; height: 900px; }

  .menu-page {
    position: absolute; top: 33px; width: 592px; height: 835px;
    background: var(--green); overflow: hidden;
  }
  .menu-page.lunch { left: 5px; }
  .menu-page.dinner { left: 603px; }

  .rays {
    position: absolute; left: 0; top: 117px; width: 100%; height: 718px;
    background:
      radial-gradient(ellipse 70% 55% at 62% 38%, var(--pale) 0%, rgba(251,249,214,0.9) 30%, rgba(245,233,74,0.55) 60%, rgba(31,138,58,0) 90%),
      linear-gradient(180deg, #fdfbe0 0%, #f2ef8a 35%, #b9d24a 62%, var(--green) 85%, var(--green-deep) 100%);
  }

  .brand { position: absolute; left: 12px; top: 62px; font-family: "Signika", sans-serif; font-weight: 400; }
  .brand-name { font-size: 22px; color: var(--gold); line-height: 1; }
  .meal-label { font-size: 12px; color: var(--white); letter-spacing: 5px; text-transform: lowercase; line-height: 1; margin-top: 8px; }

  .club-name {
    position: absolute; right: 18px; top: 48px; display: flex; align-items: center; gap: 10px;
    font-family: "Signika", sans-serif; font-weight: 600; font-size: 38px; color: var(--gold); line-height: 1;
  }
  .club-name .dot { width: 22px; height: 22px; border-radius: 50%; background: var(--gold); }

  /* lunch */
  .lunch-list { font-family: "Archivo Narrow", sans-serif; color: var(--ink); }
  .col-head { position: absolute; font-size: 9px; top: 124px; }
  .item { position: absolute; font-size: 11px; font-weight: 600; line-height: 1.15; }
  .item em { display: block; font-weight: 400; font-style: italic; padding-left: 10px; }
  .item .note { display: block; font-weight: 400; padding-left: 10px; }
  .price { position: absolute; top: 0; font-weight: 400; }
  .c1 .m { left: 182px; } .c1 .v { left: 245px; }
  .c2 .m { left: 188px; } .c2 .v { left: 252px; }

  .kids-title { position: absolute; left: 256px; top: 475px; font-size: 12px; font-weight: 600; }
  .kids { position: absolute; font-size: 10.5px; font-weight: 400; }
  .kids.b { font-weight: 600; }

  /* dinner */
  .dinner-list { font-family: "Open Sans", sans-serif; color: var(--ink); }
  .sec { position: absolute; font-weight: 800; font-size: 12.5px; letter-spacing: 1px; text-align: center; }
  .dish { position: absolute; font-size: 9.5px; font-weight: 700; letter-spacing: 0.6px; }
  .dish .p { position: absolute; top: 0; font-weight: 400; }
  .dish p { font-weight: 400; font-style: italic; font-size: 10px; letter-spacing: 0.8px; text-align: center; line-height: 1.35; margin-top: 1px; }
  .dl { left: 6px; width: 284px; }
  .dl .m { left: 185px; } .dl .v { left: 252px; }
  .dr { left: 312px; width: 272px; }
  .dr .m { left: 188px; } .dr .v { left: 248px; }
  .dhead { position: absolute; font-size: 8px; font-weight: 400; }
  .footnote { position: absolute; left: 0; width: 100%; top: 785px; text-align: center; color: var(--white); font-size: 9.5px; font-weight: 700; letter-spacing: 0.6px; }
</style>
</head>
<body>
<div class="canvas">

  <section class="menu-page lunch">
    <div class="rays" role="img" aria-label="Sunburst of yellow and green rays"></div>
    <div class="brand"><div class="brand-name">Bluegate grill</div><div class="meal-label">lunch</div></div>
    <div class="club-name"><span class="dot"></span>Kelford Hawks</div>

    <div class="lunch-list">
      <span class="col-head" style="left:188px">MEMBER</span><span class="col-head" style="left:248px">VISITOR</span>
      <span class="col-head" style="left:496px">MEMBER</span><span class="col-head" style="left:560px">VISITOR</span>

      <div class="item c1" style="left:8px;top:136px">4 Vegetarian Spring Rolls<em>with Rice</em><span class="price m">$8</span><span class="price v">$10</span></div>
      <div class="item c1" style="left:8px;top:167px">Club Sandwich<em>with Chips</em><span class="note">(chicken, bacon, cheese, tomato, lettuce &amp; mayo)</span><span class="price m">$8</span><span class="price v">$10</span></div>
      <div class="item c1" style="left:8px;top:212px">Home Made Quiche with Chips<span class="price m">$8</span><span class="price v">$10</span></div>
      <div class="item c1" style="left:8px;top:242px">T-Bone with Chips &amp; Salad<span class="price m">$10</span><span class="price v">$12</span></div>
      <div class="item c1" style="left:8px;top:258px">Open Hamburger<em>with the Works &amp; Chips</em><span class="price m">$10</span><span class="price v">$12</span></div>
      <div class="item c1" style="left:8px;top:290px">Cajun Chicken Burger<em>with Chips</em><span class="price m">$10</span><span class="price v">$12</span></div>
      <div class="item c1" style="left:8px;top:322px">Spaghetti Bolognaise<span class="price m">$10</span><span class="price v">$12</span></div>
      <div class="item c1" style="left:8px;top:341px">Chicken Caesar Salad<span class="price m">$10</span><span class="price v">$12</span></div>
      <div class="item c1" style="left:8px;top:360px">Bangers &amp; Mash<em>(1 thick &amp; 1 thin sausage)</em><span class="price m">$10</span><span class="price v">$12</span></div>
      <div class="item c1" style="left:8px;top:386px">Vegetarian Lasagne<em>with Chips &amp; Salad</em><span class="price m">$10</span><span class="price v">$12</span></div>

      <div class="item c2" style="left:315px;top:136px">Chicken or Veal Schnitzel<em>with Chips &amp; Salad</em><span class="price m">$14</span><span class="price v">$16</span></div>
      <div class="item c2" style="left:315px;top:168px">Open Steak Sandwich<em>(cheese, pineapple, egg)</em><span class="price m">$14</span><span class="price v">$16</span></div>
      <div class="item c2" style="left:315px;top:201px">All Day Breakfast<em>(sausage, egg, bacon, mushrooms,<br>tomato, hash brown &amp; toast)</em><span class="price m">$14</span><span class="price v">$16</span></div>
      <div class="item c2" style="left:315px;top:246px">Garlic Prawns<em>with Rice &amp; Salad</em><span class="price m">$14</span><span class="price v">$16</span></div>
      <div class="item c2" style="left:315px;top:278px">Beer Battered Barramundi<em>with Chips &amp; Salad</em><span class="price m">$14</span><span class="price v">$16</span></div>
      <div class="item c2" style="left:315px;top:310px">Seafood Basket<em>with Chips &amp; Salad</em><span class="price m">$14</span><span class="price v">$16</span></div>

      <div class="kids-title">KIDS MENU</div>
      <div class="kids b" style="left:85px;top:489px">Sandwiches</div>
      <div class="kids" style="left:117px;top:503px">Yeast Spread</div>
      <div class="kids" style="left:220px;top:503px">Peanut Butter</div>
      <div class="kids" style="left:357px;top:503px">Choc Hazelnut</div>
      <div class="kids" style="left:458px;top:503px">$3</div>
      <div class="kids" style="left:117px;top:522px">Strawberry Jam</div>
      <div class="kids" style="left:220px;top:522px">Devon &amp; Tomato Sauce</div>
      <div class="item" style="left:82px;top:541px;font-size:10.5px">Chicken Nuggets<em>with Chips</em></div>
      <div class="kids" style="left:458px;top:541px">$5</div>
      <div class="item" style="left:82px;top:566px;font-size:10.5px">Cheese Burger<em>with Chips</em></div>
      <div class="kids" style="left:458px;top:566px">$5</div>
    </div>
  </section>

  <section class="menu-page dinner">
    <div class="rays" role="img" aria-label="Sunburst of yellow and green rays"></div>
    <div class="brand"><div class="brand-name">Bluegate grill</div><div class="meal-label">dinner</div></div>
    <div class="club-name"><span class="dot"></span>Kelford Hawks</div>

    <div class="dinner-list">
      <div class="sec" style="left:6px;width:284px;top:124px">CHARGRILL</div>
      <span class="dhead" style="left:168px;top:141px">MEMBER</span><span class="dhead" style="left:240px;top:141px">VISITOR</span>

      <div class="dish dl" style="top:153px">MADCOW<span class="p m">$ 28</span><span class="p v">$30</span><p>A large tender rump topped with bug tail meat calamari, scallops, prawns &amp; mussels. All in a garlic white sauce</p></div>
      <div class="dish dl" style="top:215px">BBQ<span class="p m">$ 28</span><span class="p v">$30</span><p>Massive rump steak cooked the way God intended it, with bacon melted cheddar, onion rings, corn kernels and beetroot finished with a dollop of sour cream</p></div>
      <div class="dish dl" style="top:288px">CLUB SPECIAL<span class="p m">$ 28</span><span class="p v">$30</span><p>Scotch fillet steak cooked with love, topped with fried bacon fanned avocado &amp; melted camembert cheese with the sauce of your choice</p></div>
      <div class="dish dl" style="top:350px">SURF &amp; TURF<span class="p m">$ 28</span><span class="p v">$30</span><p>Tender scotch fillet steak topped with large tiger prawns in a creamy garlic sauce</p></div>
      <div class="dish dl" style="top:398px">F100 STEAK<span class="p m">$ 28</span><span class="p v">$30</span><p>Huge rump steak topped with fanned avocado, melted cheese &amp; button mushroom sauce</p></div>
      <div class="dish dl" style="top:452px">THE FULL HOUSE<span class="p m">$ 28</span><span class="p v">$30</span><p>A massive T-bone steak topped with a special seafood mix of prawns, calamari, mussels, scallops etc. with a spicy tomato &amp; basil sauce</p></div>
      <div class="dish dl" style="top:520px">CATTLEMANS STEAK<span class="p m">$ 28</span><span class="p v">$30</span><p>350g rib eye steak on the bone</p></div>
      <div class="dish dl" style="top:561px">BBQ AMERICAN PORK RIBS<span class="p m">$ 28</span><span class="p v">$30</span><p>Hickory smoked pork ribs, roasted in a BBQ sauce</p></div>
      <div class="dish dl" style="top:602px">RIB COMBO 1<span class="p m">$ 28</span><span class="p v">$30</span><p>Hickory smoked pork ribs, with char grilled chicken breast</p></div>
      <div class="dish dl" style="top:656px">RIB COMBO 2<span class="p m">$ 28</span><span class="p v">$30</span><p>Hickory smoked pork ribs, with char grilled rump steak</p></div>

      <span class="dhead" style="left:475px;top:124px">MEMBER</span><span class="dhead" style="left:546px;top:124px">VISITOR</span>
      <div class="dish dr" style="top:136px">VEAL OR CHICKEN SCHNITZEL<span class="p m">$ 20</span><span class="p v">$22</span></div>
      <div class="dish dr" style="top:155px">MIXED GRILL<span class="p m">$ 20</span><span class="p v">$22</span></div>
      <div class="dish dr" style="top:174px">RUMP STEAK 200g<span class="p m">$ 20</span><span class="p v">$22</span></div>
      <div class="dish dr" style="top:193px">RUMP STEAK 400g<span class="p m">$ 27</span><span class="p v">$29</span></div>
      <div class="dish dr" style="top:212px">T-BONE 400g<span class="p m">$ 27</span><span class="p v">$29</span></div>
      <div class="dish dr" style="top:231px">RIB FILLET 350g<span class="p m">$ 27</span><span class="p v">$29</span></div>

      <div class="sec" style="left:312px;width:272px;top:260px">VEAL</div>
      <div class="dish dr" style="top:279px">VEAL ala FUNGI<span class="p m">$ 22</span><span class="p v">$24</span><p>Succulent pan fried veal, in a creamy mushroom sauce</p></div>
      <div class="dish dr" style="top:327px">VEAL DIANE<span class="p m">$ 22</span><span class="p v">$24</span><p>Tender scallops of pan fried veal with a smooth creamy diane sauce</p></div>

      <div class="sec" style="left:312px;width:272px;top:386px">LAMB</div>
      <div class="dish dr" style="top:405px">CRUMBED LAMB CUTLETS<span class="p m">$ 25</span><span class="p v">$27</span></div>

      <div class="sec" style="left:312px;width:272px;top:434px">CHICKEN</div>
      <div class="dish dr" style="top:453px">SPECIAL NUMBER 1<span class="p m">$ 25</span><span class="p v">$27</span><p>Breast of grilled chicken served with a prawn, bacon, onion &amp; avocado garlic cream sauce</p></div>
      <div class="dish dr" style="top:501px">GARLIC CHICKEN &amp; PRAWN<span class="p m">$ 25</span><span class="p v">$27</span><p>Grilled breast of chicken topped with a creamy garlic sauce &amp; king prawns</p></div>
      <div class="dish dr" style="top:550px">CHICKEN SCALOPPINE<span class="p m">$ 25</span><span class="p v">$27</span><p>Pan fried breast of chicken with a bacon, onion, mushroom, parsley, garlic &amp; parmesan cream sauce</p></div>
      <div class="dish dr" style="top:611px">CHICKEN &amp; ASPARAGUS<span class="p m">$ 25</span><span class="p v">$27</span><p>Succulent grilled breast of chicken with garlic, asparagus &amp; Béarnaise sauce</p></div>
      <div class="dish dr" style="top:659px">CHICKEN PARMIGANA<span class="p m">$ 25</span><span class="p v">$27</span><p>Crumbed breast of chicken topped with tomato basil sauce, Finished with our own cheese mix</p></div>

      <div class="footnote">All main meals are served with chips &amp; salad or mashed potato &amp; vegetables</div>
    </div>
  </section>

</div>
</body>
</html>
```